Maple Ridge business card design

Card needs to include the following text/items:
Company Logo
Tobin Marsh
Phone # - 555-318-7642
service@mapleridgelandscaping.example
Lawn & landscape maintenance services

```html
<!DOCTYPE html>
<html lang="en">
<head>
<meta charset="utf-8">
<title>Maple Ridge Landscaping – Business Card</title>
<link rel="stylesheet" href="https://fonts.googleapis.com/css2?family=Cinzel:wght@400;600;700&display=swap">
<style>
  :root {
    --backdrop: #1c1c1c;
    --forest: #1f4a2c;
    --forest-deep: #1a3f25;
    --leaf: #7b9a2c;
    --leaf-light: #94b43a;
    --paper: #ffffff;
    --mist: #e9efeb;
    --ink: #1b1b1b;
    --cream: #f4f1e6;
  }
  * { box-sizing: border-box; margin: 0; padding: 0; }
  html, body { width: 1200px; height: 1015px; overflow: hidden; }
  body {
    background: var(--backdrop);
    font-family: "Cinzel", serif;
    position: relative;
  }
  .card {
    position: absolute;
    left: 250px;
    width: 700px;
    height: 400px;
    overflow: hidden;
  }
  /* Front */
  .card--front { top: 70px; background: var(--forest); }
  .front__scenery {
    position: absolute;
    left: 170px; top: -60px;
    width: 480px; height: 480px;
    border-radius: 50%;
    background: radial-gradient(circle at 45% 45%, rgba(255,255,255,0.08), rgba(255,255,255,0.03) 70%);
  }
  .front__band {
    position: absolute;
    left: 0; right: 0; top: 236px;
    height: 40px;
    background: var(--leaf);
    display: flex; align-items: center; justify-content: center;
  }
  .tagline {
    color: var(--cream);
    font-size: 17px;
    letter-spacing: 1.5px;
    font-weight: 600;
    text-transform: uppercase;
  }
  .brand {
    position: absolute;
    display: flex; align-items: center; gap: 18px;
  }
  .brand__mark {
    flex: none;
    width: 86px; height: 86px;
    border-radius: 50%;
    border: 3px solid var(--leaf);
  }
  .brand__name {
    font-size: 44px;
    font-weight: 700;
    letter-spacing: 1px;
    white-space: nowrap;
  }
  .card--front .brand { left: 165px; top: 108px; }
  .card--front .brand__name { color: var(--paper); }
  .card--front .brand__mark { background: var(--forest-deep); }

  /* Back */
  .card--back { top: 545px; background: var(--paper); }
  .back__scenery {
    position: absolute;
    right: 0; top: 0;
    width: 440px; height: 400px;
    background: linear-gradient(135deg, var(--mist), #f1ede4 60%, #e6ece6);
    opacity: 0.9;
  }
  .card--back .brand {
    left: 30px; top: 60px; width: 210px;
    flex-direction: column; align-items: center; gap: 12px;
  }
  .card--back .brand__mark { width: 130px; height: 130px; background: var(--mist); }
  .card--back .brand__name { color: var(--forest); font-size: 24px; }
  .contact-bar {
    position: absolute;
    left: 250px; top: 200px;
    width: 64px; height: 200px;
    background: var(--forest);
    border-radius: 16px 16px 0 0;
    display: flex; flex-direction: column; align-items: center; justify-content: center; gap: 12px;
  }
  .contact-bar svg { width: 28px; height: 28px; }
  .contact {
    position: absolute;
    left: 336px; top: 170px;
    color: var(--ink);
  }
  .contact__name {
    font-size: 30px;
    color: var(--forest);
    font-weight: 600;
    margin-bottom: 28px;
  }
  .contact__line {
    font-size: 14px;
    line-height: 30px;
    text-transform: uppercase;
    white-space: nowrap;
  }
</style>
</head>
<body>
  <section class="card card--front" aria-label="Card front">
    <div class="front__scenery" role="img" aria-label="Faint enlarged landscape scene with trees and sun"></div>
    <div class="brand">
      <span class="brand__mark"></span>
      <span class="brand__name">Maple Ridge</span>
    </div>
    <div class="front__band">
      <p class="tagline">Lawn &amp; Landscape Maintenance Services</p>
    </div>
  </section>

  <section class="card card--back" aria-label="Card back">
    <div class="back__scenery" role="img" aria-label="Faded landscape scene with bare tree, sun and fence"></div>
    <div class="brand">
      <span class="brand__mark"></span>
      <span class="brand__name">Maple Ridge</span>
    </div>
    <div class="contact-bar">
      <svg viewBox="0 0 28 28" aria-label="Phone"><circle cx="14" cy="14" r="13" fill="var(--leaf-light)"/><path d="M10 8c-1 1-1 3 1 6s4 5 6 5c1 0 2-1 2-2l-2-2-2 1-3-3 1-2-2-2z" fill="var(--forest)"/></svg>
      <svg viewBox="0 0 28 28" aria-label="Email"><circle cx="14" cy="14" r="13" fill="var(--leaf-light)"/><rect x="7" y="9" width="14" height="10" fill="none" stroke="var(--forest)" stroke-width="1.6"/><path d="M7 9l7 6 7-6" fill="none" stroke="var(--forest)" stroke-width="1.6"/></svg>
      <svg viewBox="0 0 28 28" aria-label="Website"><circle cx="14" cy="14" r="13" fill="var(--leaf-light)"/><circle cx="14" cy="14" r="7" fill="none" stroke="var(--forest)" stroke-width="1.5"/><ellipse cx="14" cy="14" rx="3" ry="7" fill="none" stroke="var(--forest)" stroke-width="1.3"/><path d="M7 14h14M8.5 10.5h11M8.5 17.5h11" stroke="var(--forest)" stroke-width="1.2"/></svg>
    </div>
    <div class="contact">
      <h1 class="contact__name">Tobin Marsh</h1>
      <p class="contact__line">555-318-7642</p>
      <p class="contact__line">service@mapleridgelandscaping.example</p>
      <p class="contact__line">www.mapleridgelandscaping.example</p>
    </div>
  </section>
</body>
</html>
```